Clean Plinth Ads Banner Design For A Finance Company

Hi,
We're a UK based finance company and are looking for new banner ads to use on the Plinth Display Network.
We want the end product to stand out by using strong, minimal design - ideally starting from a dark theme, although I'm open to ideas.
The copy should read:
'Fast Bridging Loans From 0.39% PM'
Once we have these designs agreed, we are looking to replicate them for other products, changing only the text on each ad - for example, 'commercial mortgage service you can rely on' or 'development finance service you can rely on'.
The colours used on our website are the following:
Black - #040303
Orange - #f79124
White - #ffffff
Grey - #ffffff
Example ads that I like - https://www.brimcastle.com/wp-content/uploads/2021/07/plinth-display-ads-example-2-final.png.webp
2 - https://quendrahub.com/wp-content/uploads/2020/03/fbdd56ba3bd16c7a8debb13a411de786.jpg

```html
<!DOCTYPE html>
<html lang="en">
<head>
<meta charset="utf-8">
<title>Brennoxa Finance – Fast Bridging Loans Display Banners</title>
<link rel="stylesheet" href="https://fonts.googleapis.com/css2?family=Exo+2:ital,wght@1,800&family=Barlow:wght@400;500;700&display=swap">
<style>
  :root {
    --brand-black: #040303;
    --brand-orange: #f79124;
    --brand-white: #ffffff;
    --night-navy: #0b0b3a;
    --neon-violet: #8a3fb8;
    --neon-pink: #e04fd0;
    --neon-cyan: #37d6f0;
    --city-amber: #c0703a;
    --stage: #ffffff;
  }
  * { box-sizing: border-box; margin: 0; padding: 0; }
  html, body { width: 938px; height: 1200px; overflow: hidden; background: var(--stage); }
  .canvas { position: relative; width: 938px; height: 1200px; }

  .banner {
    position: absolute;
    background: var(--brand-black);
    overflow: hidden;
    box-shadow: 6px 10px 18px rgba(0,0,0,0.28);
    font-family: "Barlow", Arial, sans-serif;
    color: var(--brand-white);
  }

  .headline {
    font-family: "Exo 2", "Arial Black", sans-serif;
    font-style: italic;
    font-weight: 800;
    text-transform: uppercase;
    letter-spacing: -0.5px;
  }
  .headline .accent { color: var(--brand-orange); }

  .cta {
    position: absolute;
    display: flex;
    align-items: center;
    justify-content: center;
    background: var(--brand-white);
    color: var(--brand-black);
    border-radius: 999px;
    font-family: "Barlow", Arial, sans-serif;
    font-weight: 500;
    letter-spacing: 1.6px;
    text-transform: uppercase;
    white-space: nowrap;
  }

  .brand-name {
    font-family: "Barlow", Arial, sans-serif;
    font-weight: 700;
    color: var(--brand-orange);
    line-height: 0.95;
    text-align: center;
  }

  /* Skyscraper banner */
  .skyscraper { left: 270px; top: 79px; width: 402px; height: 804px; }
  .skyscraper .scene {
    position: absolute; left: 0; right: 0; top: 440px; bottom: 0;
    background:
      radial-gradient(ellipse 90% 30% at 60% 55%, rgba(224,79,208,0.55), transparent 70%),
      radial-gradient(ellipse 70% 20% at 80% 92%, rgba(55,214,240,0.6), transparent 70%),
      radial-gradient(ellipse 80% 18% at 30% 78%, rgba(192,112,58,0.6), transparent 70%),
      linear-gradient(180deg, var(--brand-black) 0%, var(--night-navy) 30%, #2a1a5a 55%, #3a2040 75%, #1a1030 100%);
  }
  .skyscraper .logo-tab {
    position: absolute; left: 260px; top: 0; width: 101px; height: 72px;
    background: var(--brand-white);
    border-radius: 0 0 8px 8px;
    display: flex; align-items: center; justify-content: center;
  }
  .skyscraper .logo-tab .brand-name { font-size: 18px; }
  .skyscraper .headline { position: absolute; left: 42px; top: 28px; font-size: 68px; line-height: 70px; }
  .skyscraper .from { position: absolute; left: 40px; top: 240px; font-size: 34px; font-weight: 400; line-height: 1; }
  .skyscraper .rate {
    position: absolute; left: 38px; top: 272px;
    display: flex; align-items: flex-start;
  }
  .skyscraper .rate-value { font-size: 114px; font-weight: 700; line-height: 1; letter-spacing: -1px; }
  .skyscraper .rate-unit {
    margin-left: 14px; margin-top: 8px;
    display: flex; flex-direction: column; align-items: center;
    font-weight: 500; line-height: 1;
  }
  .skyscraper .rate-unit .percent { font-size: 44px; padding-bottom: 4px; }
  .skyscraper .rate-unit .rule { width: 46px; height: 2px; background: var(--brand-white); }
  .skyscraper .rate-unit .period { font-size: 38px; padding-top: 6px; }
  .skyscraper .cta { left: 117px; top: 720px; width: 168px; height: 39px; font-size: 19px; }

  /* Leaderboard banner */
  .leaderboard { left: 70px; top: 952px; width: 804px; height: 174px; }
  .leaderboard .scene {
    position: absolute; left: 262px; top: 0; right: 0; bottom: 0;
    background:
      radial-gradient(ellipse 45% 30% at 88% 50%, rgba(224,79,208,0.55), transparent 70%),
      radial-gradient(ellipse 30% 25% at 88% 85%, rgba(55,214,240,0.55), transparent 70%),
      radial-gradient(ellipse 50% 25% at 55% 80%, rgba(192,112,58,0.55), transparent 70%),
      linear-gradient(180deg, var(--night-navy) 0%, #22154e 60%, #120c26 100%);
    -webkit-mask-image: linear-gradient(90deg, transparent 0%, #000 45%);
    mask-image: linear-gradient(90deg, transparent 0%, #000 45%);
  }
  .leaderboard .headline { position: absolute; left: 35px; top: 22px; font-size: 40px; line-height: 1.1; white-space: nowrap; }
  .leaderboard .offer { position: absolute; left: 34px; top: 64px; font-size: 41px; line-height: 1.1; white-space: nowrap; }
  .leaderboard .offer .from { font-weight: 400; }
  .leaderboard .offer strong { font-weight: 700; }
  .leaderboard .cta { left: 34px; top: 117px; width: 127px; height: 30px; font-size: 15px; }
  .leaderboard .brand-name { position: absolute; left: 686px; top: 20px; width: 104px; font-size: 20px; }
</style>
</head>
<body>
<main class="canvas">

  <section class="banner skyscraper" aria-label="Skyscraper display banner">
    <div class="scene" role="img" aria-label="Night photo of a steel suspension bridge and city skyline with pink and cyan light trails"></div>
    <div class="logo-tab"><span class="brand-name">Brennoxa<br>Finance</span></div>
    <h1 class="headline"><span class="accent">Fast</span><br>Bridging<br>Loans</h1>
    <p class="from">From</p>
    <p class="rate">
      <span class="rate-value">0.39</span>
      <span class="rate-unit"><span class="percent">%</span><span class="rule"></span><span class="period">PM</span></span>
    </p>
    <a class="cta">Learn more</a>
  </section>

  <section class="banner leaderboard" aria-label="Leaderboard display banner">
    <div class="scene" role="img" aria-label="Night photo of a steel suspension bridge and city skyline with pink and cyan light trails"></div>
    <h2 class="headline"><span class="accent">Fast</span> Bridging Loans</h2>
    <p class="offer"><span class="from">From</span> <strong>0.39% PM</strong></p>
    <a class="cta">Learn more</a>
    <span class="brand-name">Brennoxa<br>Finance</span>
  </section>

</main>
</body>
</html>
```